Hey,
My name is Tomas Vellanegra and I'm starting a PhD in Physics next year. I want to a bit more than just research on my own. I want to bring some public involvement to it.
"Zeta Quarks" is website/wordpress/blog. It is a way to bring physics to the general public without losing the math or the physics essence - This is a place to share fun and interesting findings that PhD students, Professors, High school students and basically everyone else that loves and wants to know a bit more about nature. The idea is to put real science to debate in a open non-judgmental way in prol of knowledge and discovery. "Everybody" is welcome to post relevant things such as experiments made at home as well as their latest discovery in their super high tech £100M lab.
The first step of the project is to develop a BLOG (Wordpress) - the domain is already register "zetaquarks.org and zetaquarks.com" that could host that initial debate and posts.
Think http://lensmoravia.org/ ; http://www.wavecellar.org/; https://www.youtube.com/user/ninetyglyphs; https://www.youtube.com/user/secondquanta as a guidelines...
http://trevilo.bvx.com.br/
I would enjoy touches of watercolour design here and there.
I also like pastel colours. But remember, I am a scientist and not at all designer. I'll trust the artists to create and show me what they are up to.
UPDATE: Just so you guys know. I want to do a Website in form of a Blog. I want to easily post and upload videos and articles related to Physics.
I'm more familiar with Wordpress but if you say that any other platform does the job better and I can still maintain the domain zetaquarks.org lets do it!
Update number 2: I will respond every designer asap. I will however do that between 9:00am and 14:00 pm Brasilia/Brazil Time.
So please don't get upset or take it personal if you don't get a feedback right away, specially if it is 02:00 a.m my time, ok ?! : - )
Thanks Guys and good work!
For all designers that just want to do logos please post them in: Manage Project | Zeta Quarks - Logo Design Project
We will continue from there!
Target Market(s)
Everyone that likes physics, no matter if you are a Nobel Laureate or a single mother that likes physics.
Industry/Entity Type
Artists
Font styles to use
Other font styles liked:
- I like Calibri, Helvetica, Verdana, Univers and Tahoma for body text, Sometimes I use Arial. Cambria and Georgia for headings
Requirements
Must have
- I'm open minded! But I like thinks to be simple!
Nice to have
- The way you going to put "Zeta Quarks" is completely up to you. I usually like it simple but. Show me what you got and I'll give you feedback if I like it or not! Just remember to keep it clean and user friendly.
Should not have
- Just try beautiful and functional designs. I usually don't like super old style fonts like Times New Roman and very elaborate things that are hard to read.

```html
<!DOCTYPE html>
<html lang="en">
<head>
<meta charset="utf-8">
<title>Zeta Quarks</title>
<link href="https://fonts.googleapis.com/css2?family=Arimo:wght@400;700&family=Open+Sans:wght@400;600;700;800&display=swap" rel="stylesheet">
<style>
:root{
  --red:#e8413f;
  --red-dark:#c92f2d;
  --pink:#f06a66;
  --ink:#222;
  --muted:#666;
  --blue:#1f74b8;
  --blue-dark:#15588f;
  --bar:#3a3a3a;
  --footer:#2b2b2b;
  --footer-deep:#1c1c1c;
  --rule:#dcdcdc;
  --side:#f4f4f4;
  --orange:#f39021;
}
*{box-sizing:border-box;margin:0;padding:0}
html,body{width:763px;height:1200px;overflow:hidden}
body{font-family:"Open Sans",Arial,sans-serif;color:var(--ink);background:#fff;position:relative}
ul{list-style:none}

/* header */
.site-header{position:absolute;left:0;top:0;width:763px;height:46px;background:#fff}
.brand{position:absolute;left:18px;top:9px;font-family:"Arimo",Arial,sans-serif;font-weight:700;font-size:25px;color:var(--red);letter-spacing:-.3px}
.main-nav{position:absolute;left:326px;top:30px;display:flex}
.main-nav a{font-size:8px;color:var(--ink);text-decoration:none;padding:4px 12px;border-right:1px solid var(--rule)}
.main-nav a.is-active{background:var(--red);color:#fff;border-radius:3px 3px 0 0}
.toll{position:absolute;left:640px;top:4px;display:flex;align-items:center;gap:5px}
.toll-label{font-size:7px;color:var(--muted);line-height:1.1}
.toll-number{font-size:12px;font-weight:700;color:var(--red);display:block}

/* hero */
.hero{position:absolute;left:0;top:46px;width:763px;height:230px;background:linear-gradient(180deg,var(--pink),var(--red) 70%,var(--red-dark))}
.hero-art{position:absolute;left:64px;top:16px;width:250px;height:210px;border-radius:8px;background:radial-gradient(circle at 55% 40%,#f3d3bf 0,#6c8fbf 35%,#b44a46 75%,transparent 76%)}
.hero-copy{position:absolute;left:334px;top:30px;width:380px;color:#fff}
.hero-copy h1{font-family:"Arimo",Arial,sans-serif;font-weight:700;font-size:17px;line-height:1.3}
.hero-copy p{font-size:7.5px;line-height:1.5;margin-top:8px;opacity:.9;width:300px}
.hero-points{margin-top:8px;font-size:8px;line-height:1.7}
.hero-points li::before{content:"";display:inline-block;width:5px;height:5px;background:#ffd24a;border-radius:50%;margin-right:6px;vertical-align:middle}
.hero-cta{position:absolute;left:452px;top:190px;width:150px;height:26px;background:linear-gradient(var(--blue),var(--blue-dark));border-radius:3px;color:#fff;font-weight:800;font-size:11px;text-align:center;line-height:26px;border:1px solid #fff}

/* section bar */
.posts-bar{position:absolute;left:70px;top:284px;width:420px;height:18px;display:flex;align-items:center;justify-content:space-between}
.posts-bar h2{font-size:11px;font-weight:700;display:flex;align-items:center;gap:5px}
.bar-icon{width:14px;height:14px;border-radius:50%;background:var(--orange)}
.connect{position:absolute;left:320px;top:280px;width:175px;height:24px;background:var(--bar);border-radius:3px;display:flex;align-items:center;gap:4px;padding-left:8px}
.connect span{font-size:10px;color:#fff;font-weight:700;margin-right:4px}
.connect i{width:12px;height:12px;border-radius:2px;display:block}

/* posts */
.posts{position:absolute;left:70px;top:310px;width:420px}
.post{display:flex;height:166px;border-bottom:1px solid var(--rule);padding-top:8px}
.post-thumb{width:130px;height:100px;flex:none;margin:6px 14px 0 0;border:3px solid #eee;background:linear-gradient(135deg,#c9c0b2,#7d6f62)}
.post h3{font-family:"Arimo",Arial,sans-serif;font-weight:400;font-size:23px;line-height:1.08;width:240px}
.post p{font-size:6.5px;line-height:1.45;margin-top:6px;width:250px;color:#333}
.post p b{font-weight:700}

/* sidebar */
.sidebar{position:absolute;left:506px;top:300px;width:188px;background:var(--side);height:700px}
.side-title{font-size:11px;font-weight:700;color:var(--blue);padding:8px 8px 4px;border-bottom:1px solid var(--rule)}
.resources li{font-size:7px;color:#333;padding:4px 8px 4px 18px;border-bottom:1px dotted var(--rule);position:relative}
.resources li::before{content:"";position:absolute;left:8px;top:7px;border-left:4px solid var(--blue);border-top:2.5px solid transparent;border-bottom:2.5px solid transparent}
.latest{padding:4px 8px}
.latest-item{display:flex;gap:5px;margin:6px 0}
.latest-thumb{width:40px;height:34px;flex:none;background:linear-gradient(135deg,#a9b8c8,#5d6f84)}
.latest-item p{font-size:6px;line-height:1.4;color:#444}
.latest-item b{color:var(--blue)}
.badges{display:grid;grid-template-columns:repeat(4,40px);gap:4px;padding:6px 8px}
.badges i{height:34px;display:block;border-radius:2px}
.tags-head{margin:14px 0 0 -8px;width:196px;height:22px;background:linear-gradient(var(--blue),var(--blue-dark));color:#fff;font-size:12px;font-weight:700;padding:3px 10px;border-radius:0 3px 3px 0;display:flex;align-items:center;gap:6px}
.tags-head::before{content:"";width:10px;height:10px;border-radius:50%;background:#fff}
.tag-cloud{padding:10px 8px;line-height:1.35;color:#333}
.tag-cloud span{display:inline-block;margin-right:6px}
.t-xl{font-size:17px;font-weight:700}
.t-lg{font-size:13px;font-weight:600}
.t-md{font-size:11px}
.t-sm{font-size:8px}

/* footer */
.site-footer{position:absolute;left:0;top:1008px;width:763px;height:166px;background:var(--footer);color:#ddd}
.footer-col{position:absolute;top:16px}
.footer-col h4{font-size:9px;font-weight:800;color:#fff;margin-bottom:6px}
.footer-col li{font-size:6.5px;line-height:1.9}
.footer-col li::before{content:"› ";color:var(--red)}
.col-categories{left:70px}
.col-policies{left:228px}
.col-address{left:355px}
.footer-map{position:absolute;left:478px;top:18px;width:214px;height:130px;background:linear-gradient(135deg,#e8e3d6,#c9d7c2);border:2px solid #555}
.bottom-nav{position:absolute;left:0;top:1174px;width:763px;height:26px;background:var(--footer-deep);display:flex;justify-content:center;align-items:center;gap:22px}
.bottom-nav a{font-size:6.5px;color:#bbb;text-decoration:none;font-weight:600}
</style>
</head>
<body>

<header class="site-header">
  <div class="brand">Zeta Quarks</div>
  <nav class="main-nav">
    <a href="#" class="is-active">Home</a>
    <a href="#">Did You Know?</a>
    <a href="#">GE Secret Lessons</a>
    <a href="#">Recommend</a>
    <a href="#">About</a>
  </nav>
  <div class="toll">
    <svg width="18" height="18" viewBox="0 0 18 18" aria-hidden="true"><circle cx="9" cy="9" r="9" fill="#e8413f"/><path d="M6 4.5c.6 0 1 .9 1.4 1.8.2.5-.5.9-.7 1.2.5 1.2 1.4 2.1 2.6 2.7.3-.2.7-.9 1.2-.7.9.4 1.8.8 1.8 1.4 0 .9-1 1.8-2 1.6C7.8 12 5.8 10 5.3 7.5 5 6.5 5.3 4.5 6 4.5z" fill="#fff"/></svg>
    <div class="toll-label">TOLL FREE NO<span class="toll-number">1800-555-0142</span></div>
  </div>
</header>

<section class="hero">
  <div class="hero-art" role="img" aria-label="Illustration of a smiling student standing beside a stack of books and a trophy"></div>
  <div class="hero-copy">
    <h1>This website provides physics resources for students at School and the public at large.</h1>
    <p>We share clear physics explanations, useful pages and simple notes for every curious reader who wants the basics and then goes a little deeper.</p>
    <ul class="hero-points">
      <li>Essentials</li>
      <li>Lessons</li>
      <li>Case Study</li>
      <li>Lectures</li>
    </ul>
  </div>
  <div class="hero-cta">WHY ZETA QUARKS</div>
</section>

<div class="posts-bar"><h2><span class="bar-icon"></span>Lastest Posts</h2></div>
<div class="connect">
  <span>Connect with us:</span>
  <i style="background:#3b5998"></i><i style="background:#55acee"></i><i style="background:#dd4b39"></i><i style="background:#0e76a8"></i><i style="background:#f39021"></i><i style="background:#cc2127"></i>
</div>

<main class="posts">
  <article class="post">
    <div class="post-thumb" role="img" aria-label="Photo of a teacher at a whiteboard"></div>
    <div><h3>Why the Sky is Blue explained in ten seconds</h3>
    <p><b>Business Communication</b> Headline News: Find out what's going on in the world of corporate and business with our fixed detection services and how do you manage. What are fixed detection services and how do you manage communications.</p></div>
  </article>
  <article class="post">
    <div class="post-thumb" role="img" aria-label="Photo of students working together at a desk"></div>
    <div><h3>Why the Sky is Blue explained in ten seconds</h3>
    <p><b>Business Communication</b> Headline News: Find out what's going on in the world of corporate and business with our fixed detection services and how do you manage. What are fixed detection services and how do you manage communications.</p></div>
  </article>
  <article class="post">
    <div class="post-thumb" role="img" aria-label="Photo of a lecturer presenting to a class"></div>
    <div><h3>Why the Sky is Blue explained in ten seconds</h3>
    <p><b>Business Communication</b> Headline News: Find out what's going on in the world of corporate and business with our fixed detection services and how do you manage. What are fixed detection services and how do you manage communications.</p></div>
  </article>
  <article class="post">
    <div class="post-thumb" role="img" aria-label="Photo of a physics classroom experiment"></div>
    <div><h3>Why the Sky is Blue explained in ten seconds</h3>
    <p><b>Business Communication</b> Headline News: Find out what's going on in the world of corporate and business with our fixed detection services and how do you manage. What are fixed detection services and how do you manage communications.</p></div>
  </article>
</main>

<aside class="sidebar">
  <h3 class="side-title">Helpful Resources</h3>
  <ul class="resources">
    <li>Theoretical Tips</li>
    <li>Mass Docs</li>
    <li>Widgeted Docs</li>
    <li>CDN Docs</li>
    <li>JCH Download</li>
    <li>Social Icons Download</li>
    <li>Menu Icons Download</li>
  </ul>
  <h3 class="side-title">Latest Post</h3>
  <div class="latest">
    <div class="latest-item"><div class="latest-thumb" role="img" aria-label="Small post photo"></div><p><b>WP</b> Building a simple pendulum at home with string, weights and a timer.</p></div>
    <div class="latest-item"><div class="latest-thumb" role="img" aria-label="Small post photo"></div><p><b>WP</b> Measuring the speed of sound in your kitchen with two phones.</p></div>
  </div>
  <div class="badges">
    <i style="background:#3b5998"></i><i style="background:#55acee"></i><i style="background:#dd4b39"></i><i style="background:#0e76a8"></i>
    <i style="background:#f39021"></i><i style="background:#cc2127"></i><i style="background:#6a9e2f"></i><i style="background:#555"></i>
  </div>
  <div class="tags-head">Tags</div>
  <div class="tag-cloud">
    <span class="t-xl">Negotiate</span><span class="t-sm">Pricing</span>
    <span class="t-sm">Banking fees</span><span class="t-lg">Tricks Tips</span>
    <span class="t-lg">Best Treasury Advisors</span>
    <span class="t-sm">Earnings Credit Rates</span><span class="t-md">Tools</span>
    <span class="t-lg">Service Definitions</span>
    <span class="t-md">Treasury Consultant</span>
  </div>
</aside>

<footer class="site-footer">
  <div class="footer-col col-categories"><h4>CATEGORIES</h4>
    <ul><li>Did You Know?</li><li>ABOUT US</li><li>IMPRINT</li><li>WORK WITH US</li><li>Home</li></ul></div>
  <div class="footer-col col-policies"><h4>POLICIES</h4>
    <ul><li>Privacy Policy</li><li>Refund Policy</li><li>Copyright</li><li>External Link Policy</li><li>Anti Spam Policy</li><li>DCMA Disclaimer</li></ul></div>
  <div class="footer-col col-address"><h4>ADDRESS</h4>
    <ul><li>48 Ridgefield Ave</li><li>Suite 12</li><li>Harlow Bay, NC 27000</li></ul></div>
  <div class="footer-map" role="img" aria-label="Map showing the office location"></div>
</footer>
<nav class="bottom-nav">
  <a href="#">HOME</a><a href="#">ABOUT US</a><a href="#">THE TEAM</a><a href="#">RESUME TIPS</a><a href="#">TIMESHEETS</a><a href="#">SEND RESUME</a><a href="#">CANDIDATES</a><a href="#">LOCATION</a><a href="#">CONTACT US</a>
</nav>

</body>
</html>
```